Commercial Broker Profile Flyer

I need a one-page flyer created that will serve as a profile report for individual brokers within a commercial real estate firm. The flyer will include company branding, agent photo, bio, and other information. I would like to have the source file available for future editing preferably in a Publisher file format. A copy of a company brochure is included and would like to have this profile flyer similar to keep company branding consistent. Our company website is www.coltbrinwellre.com for any other questions on branding.

Target Market(s)

Professional

Industry/Entity Type

Real Estate Agent

Requirements
Must have
• One page
• Source files MUST include a .PUB file that I can update in the future
• All of the information in the uploaded "content" file
• Company branding
• Must be 8.5"x11"
Should not have
• Do not use stock photos or property photos from the attachments. I only want the broker photo and company logo.

```html
<!DOCTYPE html>
<html lang="en">
<head>
<meta charset="utf-8">
<title>Broker Profile – Nathan Brinwell</title>
<link href="https://fonts.googleapis.com/css2?family=Figtree:wght@400;800&display=swap" rel="stylesheet">
<style>
  :root {
    --brand-green: #0d5a37;
    --body-gray: #5a5a5a;
    --panel-gray: #d3d4d6;
    --frame-gray: #d0d1d3;
    --photo-tone-a: #8b8f8c;
    --photo-tone-b: #6f7370;
    --backdrop: #3a3939;
    --paper: #ffffff;
  }
  * { box-sizing: border-box; margin: 0; padding: 0; }
  html, body {
    width: 1200px; height: 1200px; overflow: hidden;
    background: var(--backdrop);
    font-family: "Figtree", Arial, sans-serif;
  }
  .flyer {
    position: absolute; left: 136px; top: 0;
    width: 927px; height: 1200px;
    background: var(--paper);
    overflow: hidden;
  }
  .header-wave { position: absolute; left: 0; top: 0; }
  .brand {
    position: absolute; left: 58px; top: 57px;
    display: flex; align-items: center; gap: 10px;
  }
  .brand-dot {
    width: 76px; height: 76px; border-radius: 50%;
    background: var(--brand-green);
  }
  .brand-name {
    color: var(--brand-green); font-weight: 400;
    font-size: 36px; line-height: 1.05;
  }
  .section-title {
    color: var(--brand-green); font-weight: 800;
    font-size: 17px; letter-spacing: 0.2px; line-height: 22px;
  }
  .body-copy {
    color: var(--body-gray); font-size: 17px; line-height: 21.8px;
  }
  .bio { position: absolute; left: 62px; top: 242px; width: 402px; }
  .clients { position: absolute; left: 62px; top: 744px; width: 360px; }
  .affiliations { position: absolute; left: 62px; top: 984px; width: 345px; }
  .plain-list { list-style: none; }
  .portrait-frame {
    position: absolute; left: 557px; top: 244px;
    width: 318px; height: 448px;
    background: var(--frame-gray); padding: 7px;
  }
  .portrait {
    width: 100%; height: 100%;
    background: linear-gradient(160deg, var(--photo-tone-a), var(--photo-tone-b));
  }
  .broker-name {
    position: absolute; right: 52px; top: 788px;
    color: var(--brand-green); font-size: 60px; line-height: 1;
    font-weight: 400; letter-spacing: -0.5px; white-space: nowrap;
  }
  .broker-name strong { font-weight: 800; }
  .contact-panel {
    position: absolute; left: 557px; top: 947px;
    width: 370px; height: 253px;
    background: var(--panel-gray);
    padding: 28px 0 0 36px;
  }
  .contact-panel .section-title { margin-bottom: 22px; }
  .contact-lines {
    list-style: none; color: var(--brand-green);
    font-size: 17px; line-height: 21.8px;
  }
</style>
</head>
<body>
  <main class="flyer">
    <svg class="header-wave" width="927" height="210" viewBox="0 0 927 210" aria-hidden="true">
      <path d="M0,0 H878 C780,10 700,60 600,110 C480,170 380,210 260,201 C150,194 80,140 0,136 Z" fill="var(--panel-gray)"/>
    </svg>

    <div class="brand">
      <span class="brand-dot"></span>
      <span class="brand-name">Colt-Brinwell<br>Real Estate</span>
    </div>

    <section class="bio">
      <h2 class="section-title">BIO</h2>
      <p class="body-copy">Nathan began his real estate career in 2005 and has completed $75+ million in transactions representing sellers and buyers of commercial real estate, providing tenant representation, and leasing of retail and office properties. Prior to beginning his real estate career, Nathan served over five years in the Army Reserves and attended Carolina Piedmont University.<br>Nathan has earned the prestigious Certified Commercial Property Advisor (CCPA) designation as well as the Certified Leasing Professional (CLP) designation. Nathan is a member of the Regional Council of Retail Centers (RCRC), the Tri-County and Harlow Realtor Association, the Harlow-Pine County Chamber of Commerce, and serves on the board of directors for the State CCPA Chapter, the Sandhills Community Fitness League, and the Pinecrest Realtors Association. Nathan is a licensed real estate broker in NC and SC.</p>
    </section>

    <div class="portrait-frame">
      <div class="portrait" role="img" aria-label="Head-and-shoulders portrait of the broker in a grey suit against a grey studio backdrop"></div>
    </div>

    <section class="clients">
      <h2 class="section-title">CLIENTS SERVED</h2>
      <ul class="plain-list body-copy">
        <li>Hollowbrook Kitchen</li>
        <li>Crestfield Burger Co.</li>
        <li>Trimvale Cuts</li>
        <li>Tarrow Tire Depot</li>
        <li>Petite Crumb</li>
        <li>Larkmere Healthcare</li>
        <li>Family Wayfarers</li>
        <li>Brookline Edge</li>
        <li>Corvane Bottling Ventures</li>
      </ul>
    </section>

    <h1 class="broker-name">Nathan <strong>Brinwell</strong></h1>

    <section class="affiliations">
      <h2 class="section-title">PROFESSIONAL AFFILIATIONS</h2>
      <ul class="plain-list body-copy">
        <li>Certified Commercial Property Advisor (designee)</li>
        <li>Regional Council of Retail Centers</li>
        <li>Pinecrest Realtors Association</li>
        <li>State Realtors Commercial Forms Committee</li>
      </ul>
    </section>

    <aside class="contact-panel">
      <h2 class="section-title">CONTACT INFORMATION</h2>
      <ul class="contact-lines">
        <li>T. Nathan Brinwell, CCPA, CLP</li>
        <li>Principal / Broker in Charge</li>
        <li>Office Phone: (555) 014-2730 ext. 202</li>
        <li>Cell Phone:&nbsp; (555) 017-6649</li>
        <li>Email: nathan@coltbrinwellre.com</li>
        <li>Website: www.coltbrinwellre.com</li>
      </ul>
    </aside>
  </main>
</body>
</html>
```